Money transfer app

I want a redesign of 3-4 screens of the mobile app.

I want:
1. Splash screen
2. Welcome screen
3. Login screen
4. More options. to send screen

I have attached existing designs.

```html
<!DOCTYPE html>
<html lang="en">
<head>
<meta charset="utf-8">
<title>Swift Send – onboarding screens</title>
<link href="https://fonts.googleapis.com/css2?family=Outfit:wght@300;400;500;600;700&display=swap" rel="stylesheet">
<style>
  :root {
    --stage: #8eadd6;
    --forest: #0a3300;
    --lime: #86e85a;
    --mint: #e4f9dc;
    --ink: #111511;
    --muted: #8a8f8a;
    --line: #dfe3df;
    --link: #2354e6;
    --white: #ffffff;
  }
  * { margin: 0; padding: 0; box-sizing: border-box; }
  html, body { width: 1200px; height: 604px; overflow: hidden; }
  body {
    background: var(--stage);
    font-family: "Outfit", sans-serif;
    color: var(--ink);
    position: relative;
  }
  .screen {
    position: absolute;
    top: 43px;
    width: 179px;
    height: 388px;
    background: var(--white);
    overflow: hidden;
    box-shadow: 0 18px 30px rgba(40, 70, 130, .18);
  }
  .screen > * { position: absolute; }
  .screen--splash { left: 41px; background: var(--forest); }
  .screen--welcome { left: 229px; }
  .screen--register { left: 416px; height: 518px; }
  .screen--login { left: 604px; }
  .screen--verify { left: 792px; }
  .screen--verify-filled { left: 980px; }

  .status { top: 7px; left: 9px; right: 9px; height: 8px; display: flex; justify-content: space-between; align-items: center; font-size: 7.5px; font-weight: 600; }
  .screen--splash .status { color: var(--white); }
  .status svg { width: 34px; height: 7px; }

  .back { left: 10px; top: 31px; width: 11px; height: 10px; }

  .brand { top: 181px; left: 0; right: 0; display: flex; justify-content: center; align-items: center; gap: 5px; color: var(--white); font-size: 16px; font-weight: 500; }
  .brand-dot { width: 20px; height: 20px; border-radius: 50%; border: 2px solid var(--lime); }

  .hero { left: 0; top: 0; width: 179px; height: 153px; border-radius: 0 0 50% 50% / 0 0 18% 18%; background: linear-gradient(180deg, #e6fadf 0%, #d2f5c3 100%); }
  .hero-art { left: 30px; top: 46px; width: 118px; height: 86px; border-radius: 10px; background: linear-gradient(135deg, var(--lime) 0%, #4fae2c 55%, var(--forest) 100%); }

  .welcome-title { top: 187px; left: 0; right: 0; text-align: center; font-size: 20px; font-weight: 600; color: var(--forest); letter-spacing: -.4px; }
  .welcome-brand { top: 208px; left: 0; right: 0; text-align: center; font-size: 26px; font-weight: 700; color: var(--lime); letter-spacing: -.6px; }
  .tagline { top: 249px; left: 16px; right: 16px; text-align: center; font-size: 7.5px; font-weight: 300; line-height: 11px; }
  .tagline b { font-weight: 500; }

  .btn { left: 13px; width: 153px; height: 28px; border-radius: 4px; background: var(--lime); display: flex; align-items: center; justify-content: center; font-size: 8.5px; font-weight: 600; color: var(--forest); }
  .foot { left: 0; right: 0; text-align: center; font-size: 7.5px; }
  .foot a { color: var(--link); text-decoration: underline; }
  .foot a.plain { text-decoration: none; }

  .title { left: 10px; font-size: 15px; font-weight: 600; letter-spacing: -.3px; }
  .subtitle { left: 10px; font-size: 7.5px; font-weight: 300; color: var(--muted); }
  .label { left: 10px; font-size: 7.5px; font-weight: 500; }
  .field { left: 10px; width: 159px; height: 29px; border: 1px solid var(--line); border-radius: 4px; display: flex; align-items: center; font-size: 6.5px; color: var(--muted); }
  .field .ico { width: 8px; height: 8px; margin: 0 5px 0 7px; }
  .field .sep { width: 1px; height: 11px; background: var(--line); margin-right: 5px; }
  .field .eye { width: 8px; height: 8px; margin-left: auto; margin-right: 8px; }

  .divider { top: 382px; left: 45px; width: 89px; display: flex; align-items: center; gap: 6px; font-size: 6.5px; }
  .divider span { flex: 1; height: 1px; background: #eef0ee; }
  .signup-with { top: 396px; left: 0; right: 0; text-align: center; font-size: 6.5px; color: var(--muted); }
  .social { top: 416px; width: 72px; height: 22px; border: 1px solid var(--line); border-radius: 11px; display: flex; align-items: center; justify-content: center; gap: 4px; font-size: 8px; }
  .social i { width: 8px; height: 8px; border-radius: 50%; background: var(--forest); }
  .social--mail { left: 12px; }
  .social--net { left: 95px; }

  .forgot { top: 210px; right: 10px; font-size: 5.5px; color: var(--link); text-decoration: underline; }

  .verify-title { left: 18px; top: 140px; font-size: 12px; font-weight: 600; }
  .verify-text { left: 18px; top: 157px; width: 130px; font-size: 7px; font-weight: 300; color: var(--muted); line-height: 11px; }
  .verify-text b { font-weight: 400; color: var(--ink); }
  .code { top: 192px; left: 18px; display: flex; gap: 7px; }
  .code span { width: 30px; height: 28px; border-radius: 4px; background: #f6f7f6; display: flex; align-items: center; justify-content: center; font-size: 7px; font-weight: 500; }
  .code .done { background: var(--lime); }
  .code .active { background: var(--mint); border: 1px solid var(--lime); }
  .small { left: 18px; font-size: 5.5px; font-weight: 300; color: #6d726d; }
  .small a { color: var(--forest); font-weight: 500; text-decoration: underline; }
</style>
</head>
<body>

<svg width="0" height="0" style="position:absolute">
  <defs>
    <symbol id="status-icons" viewBox="0 0 34 7">
      <rect x="0" y="5" width="1.4" height="2" fill="currentColor"/><rect x="2" y="3.8" width="1.4" height="3.2" fill="currentColor"/><rect x="4" y="2.4" width="1.4" height="4.6" fill="currentColor"/><rect x="6" y="1" width="1.4" height="6" fill="currentColor"/>
      <path d="M10 3 Q13.5 0 17 3 M11.3 4.4 Q13.5 2.6 15.7 4.4" stroke="currentColor" stroke-width="1" fill="none"/><circle cx="13.5" cy="6" r=".8" fill="currentColor"/>
      <rect x="21" y="1" width="11" height="5" rx="1.2" fill="currentColor"/><rect x="32.5" y="2.6" width="1" height="1.8" fill="currentColor"/>
    </symbol>
    <symbol id="back-arrow" viewBox="0 0 11 10"><path d="M10.5 5H1M5 1 1 5l4 4" stroke="#111" stroke-width="1" fill="none"/></symbol>
    <symbol id="ico-user" viewBox="0 0 8 8"><circle cx="4" cy="2.4" r="1.7" stroke="#888" stroke-width=".7" fill="none"/><path d="M1 7.6c.4-2 5.6-2 6 0z" stroke="#888" stroke-width=".7" fill="none"/></symbol>
    <symbol id="ico-mail" viewBox="0 0 8 8"><circle cx="4" cy="4" r="3.5" stroke="#888" stroke-width=".7" fill="none"/><path d="M2 3.2 4 4.6 6 3.2" stroke="#888" stroke-width=".7" fill="none"/></symbol>
    <symbol id="ico-phone" viewBox="0 0 8 8"><path d="M1.5 1 3 1 3.6 2.8 2.7 3.5Q3.7 5.3 4.6 5.4L5.3 4.5 7 5.1 7 6.6Q4 7.6 1 2.6z" stroke="#888" stroke-width=".7" fill="none"/></symbol>
    <symbol id="ico-lock" viewBox="0 0 8 8"><rect x="1.5" y="3.4" width="5" height="4" rx="1.5" stroke="#888" stroke-width=".7" fill="none"/><path d="M2.7 3.4V2.4a1.3 1.3 0 0 1 2.6 0v1" stroke="#888" stroke-width=".7" fill="none"/></symbol>
    <symbol id="ico-eye" viewBox="0 0 8 8"><circle cx="4" cy="4" r="3.4" stroke="#888" stroke-width=".7" fill="none"/><circle cx="4" cy="4" r="1.3" stroke="#888" stroke-width=".7" fill="none"/></symbol>
    <symbol id="ico-eye-off" viewBox="0 0 8 8"><path d="M.6 4Q4 .2 7.4 4 4 7.8.6 4z" stroke="#888" stroke-width=".7" fill="none"/><circle cx="4" cy="4" r="1.2" stroke="#888" stroke-width=".7" fill="none"/><path d="M1 7 7 1" stroke="#888" stroke-width=".7"/></symbol>
  </defs>
</svg>

<!-- Splash -->
<section class="screen screen--splash">
  <div class="status"><span>9:41</span><svg><use href="#status-icons"/></svg></div>
  <div class="brand"><span class="brand-dot"></span>swiftsend</div>
</section>

<!-- Welcome -->
<section class="screen screen--welcome">
  <div class="hero"></div>
  <div class="hero-art" role="img" aria-label="Illustration: a person sending money from a phone to a bank, with a shield and coins"></div>
  <div class="status"><span>9:41</span><svg><use href="#status-icons"/></svg></div>
  <h1 class="welcome-title">Welcome to</h1>
  <p class="welcome-brand">Swift Send</p>
  <p class="tagline">Sending money made <b>Simple, Fast &amp; Transparent.</b></p>
  <div class="btn" style="top:300px">Login</div>
  <p class="foot" style="top:343px">Don’t have an account? <a>Register</a></p>
</section>

<!-- Register -->
<section class="screen screen--register">
  <div class="status"><span>9:41</span><svg><use href="#status-icons"/></svg></div>
  <svg class="back"><use href="#back-arrow"/></svg>
  <h2 class="title" style="top:52px">Register</h2>
  <p class="subtitle" style="top:73px">Welcome back to the app</p>
  <p class="label" style="top:100px">Name</p>
  <div class="field" style="top:115px"><svg class="ico"><use href="#ico-user"/></svg><span class="sep"></span>Enter full Name</div>
  <p class="label" style="top:156px">Email Address</p>
  <div class="field" style="top:171px"><svg class="ico"><use href="#ico-mail"/></svg><span class="sep"></span>Enter Email address</div>
  <p class="label" style="top:212px">Phone Number</p>
  <div class="field" style="top:227px"><svg class="ico"><use href="#ico-phone"/></svg><span class="sep"></span>+92</div>
  <p class="label" style="top:268px">Password</p>
  <div class="field" style="top:283px"><svg class="ico"><use href="#ico-lock"/></svg><span class="sep"></span>Enter Password<svg class="eye"><use href="#ico-eye-off"/></svg></div>
  <div class="btn" style="top:337px">Login</div>
  <div class="divider"><span></span>or<span></span></div>
  <p class="signup-with">Sign up with</p>
  <div class="social social--mail"><i></i>Mailbox</div>
  <div class="social social--net"><i></i>Social</div>
  <p class="foot" style="top:457px">Already have an account? <a class="plain">Login</a></p>
</section>

<!-- Login -->
<section class="screen screen--login">
  <div class="status"><span>9:41</span><svg><use href="#status-icons"/></svg></div>
  <svg class="back" style="top:41px"><use href="#back-arrow"/></svg>
  <h2 class="title" style="top:61px">Login</h2>
  <p class="subtitle" style="top:83px">Welcome back to the app</p>
  <p class="label" style="top:109px">Email Address</p>
  <div class="field" style="top:123px"><svg class="ico"><use href="#ico-mail"/></svg>Enter Email address</div>
  <p class="label" style="top:161px">Password</p>
  <div class="field" style="top:176px"><svg class="ico"><use href="#ico-lock"/></svg>Enter Password<svg class="eye"><use href="#ico-eye"/></svg></div>
  <a class="forgot">Forgot Password</a>
  <div class="btn" style="top:251px">Login</div>
  <p class="foot" style="top:300px;left:10px;text-align:left">Don’t have an account? <a>Register</a></p>
</section>

<!-- Verify -->
<section class="screen screen--verify">
  <div class="status"><span>9:41</span><svg><use href="#status-icons"/></svg></div>
  <svg class="back"><use href="#back-arrow"/></svg>
  <h2 class="verify-title">Verify Code</h2>
  <p class="verify-text">Check your SMS inbox, we have sent you the code at <b>(+0 000 000 0000)</b></p>
  <div class="code"><span>-</span><span>-</span><span>-</span><span>-</span></div>
  <p class="small" style="top:230px">Didn’t receive a code? <a>Resend Code</a></p>
</section>

<!-- Verify, partly entered -->
<section class="screen screen--verify-filled">
  <div class="status"><span>9:41</span><svg><use href="#status-icons"/></svg></div>
  <svg class="back"><use href="#back-arrow"/></svg>
  <h2 class="verify-title">Verify Code</h2>
  <p class="verify-text">Check your SMS inbox, we have sent you the code at <b>(+0 000 000 0000)</b></p>
  <div class="code"><span class="done">1</span><span class="active">2</span><span>-</span><span>-</span></div>
  <p class="small" style="top:225px;color:var(--ink)">(00:52)</p>
  <p class="small" style="top:242px">This session will end in 60 seconds.</p>
  <p class="small" style="top:252px">Didn’t receive a code? <a>Resend Code</a></p>
</section>

</body>
</html>
```